Business Card Design Project

Hello Designers, hope you are all aiming enjoy the weekend
I have the Business Logo (uploaded), you can alter the color which ever way you think would work,
Im looking for a simple yet striking feel, something which will stay memorable (I have uploaded 3 examples for you to flick through)
Information on the card, will just be the bare minimum,
Double Sided
Info being
i.e.
Name
Number
Website
ABN
Tobin Wexmoor
+468213579 (singapore)
+315792846 (Australia)
+729384615 (America)
www.lomevu-linkup.example
ABN 86420913
Enjoy,
Tobin
Industry/Entity Type
Business
Look and feel
Each slider illustrates characteristics of the customer's brand and the style your logo design should communicate.

```html
<!DOCTYPE html>
<html lang="en">
<head>
<meta charset="utf-8">
<title>Lomevu Linkup – Business Card</title>
<link rel="stylesheet" href="https://fonts.googleapis.com/css2?family=Ubuntu:wght@500&display=swap">
<style>
  :root {
    --page: #ffffff;
    --card: #d1cbbf;
    --card-shade: #c8c1b4;
    --ink: #6a6868;
    --teal: #2a9ca8;
    --icon: #5f5d5b;
  }
  * { margin: 0; padding: 0; box-sizing: border-box; }
  html, body {
    width: 1200px;
    height: 374px;
    overflow: hidden;
    background: var(--page);
  }
  .sheet {
    position: relative;
    width: 1200px;
    height: 374px;
    font-family: "Ubuntu", "Trebuchet MS", sans-serif;
  }
  .card {
    position: absolute;
    top: 0;
    width: 578px;
    height: 374px;
    border-radius: 30px;
    background: radial-gradient(circle at 40% 35%, var(--card) 0%, var(--card-shade) 100%);
  }
  .card--front { left: 0; }
  .card--back { left: 622px; }

  .brand {
    position: absolute;
    display: flex;
    align-items: center;
    gap: 16px;
    color: var(--teal);
    font-weight: 500;
    white-space: nowrap;
  }
  .brand__mark {
    width: 40px;
    height: 40px;
    background: var(--teal);
  }
  .card--front .brand {
    left: 70px;
    top: 282px;
    font-size: 50px;
    letter-spacing: 1px;
  }
  .card--back .brand {
    left: 0;
    right: 0;
    top: 82px;
    justify-content: center;
    font-size: 40px;
  }

  .contact {
    position: absolute;
    left: 84px;
    top: 228px;
    color: var(--ink);
    font-size: 19px;
    font-weight: 500;
    line-height: 29px;
  }
  .contact__row { white-space: nowrap; }
  .contact__abn { margin-left: 30px; }
  .contact__icon {
    position: absolute;
    fill: var(--icon);
  }
  .contact__icon--phone { left: 32px; top: 222px; }
  .contact__icon--web { left: 30px; top: 313px; }
</style>
</head>
<body>
<main class="sheet">
  <section class="card card--front">
    <div class="brand">
      <span>Lomevu</span><span class="brand__mark" aria-hidden="true"></span><span>Linkup</span>
    </div>
  </section>

  <section class="card card--back">
    <div class="brand"><span>Lomevu Linkup</span></div>

    <svg class="contact__icon contact__icon--phone" width="28" height="26" viewBox="0 0 28 26" aria-hidden="true">
      <path d="M2 6 Q14 -1 26 6 L26 9 L20 9 L20 6 Q14 4 8 6 L8 9 L2 9 Z"/>
      <path d="M5 11 H23 L26 24 H2 Z"/>
      <circle cx="14" cy="17" r="3.5" fill="#d1cbbf"/>
    </svg>

    <svg class="contact__icon contact__icon--web" width="32" height="32" viewBox="0 0 32 32" aria-hidden="true">
      <circle cx="16" cy="16" r="14"/>
      <path d="M8 8 Q13 6 14 10 Q12 14 8 13 Z M17 5 Q24 6 27 12 Q22 13 20 10 Q17 9 17 5 Z M15 17 Q21 16 22 21 Q19 27 16 27 Q14 22 15 17 Z" fill="#d1cbbf"/>
    </svg>

    <div class="contact">
      <p class="contact__row">+468213579 (Singapore)</p>
      <p class="contact__row">+315792846 (Australia)</p>
      <p class="contact__row">+729384615 (America)</p>
      <p class="contact__row">www.lomevu-linkup.example<span class="contact__abn">ABN 86420913</span></p>
    </div>
  </section>
</main>
</body>
</html>
```